I'm an electrician and the name of my company is called Brisk 'N' Bright Electrical. I require a professional business card that speaks to my clients, I also need it to be innovative and modern. We do maintenance & service work for domestic and commercial premises.

Industry/Entity Type

Electrical

Contact Information for Business Card

Must have the name of my company Brisk 'N' Bright Electrical, my name Darren Kolovos and my contact details 0427 381 592 and company email address Brisknbrightelectrical@mailvane.com and/or website Brisknbrightelectrical.com.au

Logo Text

Brisk 'N' Bright Electrical (If possible)

Colors
33a6d7
0592cd
3176b5

```html
<!DOCTYPE html>
<html lang="en">
<head>
<meta charset="utf-8">
<title>Brisk 'N' Bright Electrical – Business Card</title>
<link rel="stylesheet" href="https://fonts.googleapis.com/css2?family=Montserrat:wght@400;500;700;800&display=swap">
<style>
  :root {
    --bg: #2b2b2d;
    --paper: #f2f2f3;
    --ink: #1e1e20;
    --ink-soft: #2e2e31;
    --blue: #33a6d7;
    --blue-deep: #0592cd;
    --shadow: rgba(0, 0, 0, 0.55);
  }
  * { box-sizing: border-box; margin: 0; padding: 0; }
  html, body {
    width: 1200px;
    height: 900px;
    overflow: hidden;
    background: var(--bg);
    font-family: "Montserrat", sans-serif;
  }
  .stage {
    position: relative;
    width: 1200px;
    height: 900px;
  }
  .card {
    position: absolute;
    width: 560px;
    height: 320px;
    background: var(--paper);
    box-shadow: 0 24px 40px var(--shadow);
  }
  .card--front { left: 290px; top: 80px; }
  .card--back  { left: 350px; top: 490px; }

  /* wordmark */
  .wordmark {
    display: flex;
    align-items: center;
    gap: 10px;
  }
  .wordmark__dot {
    width: 14px;
    height: 14px;
    border-radius: 50%;
    background: var(--blue-deep);
    flex: none;
  }
  .wordmark__name {
    font-weight: 800;
    color: var(--ink);
    text-transform: uppercase;
    letter-spacing: 0.02em;
    line-height: 1.1;
  }

  /* front */
  .card--front .wordmark {
    position: absolute;
    right: 44px;
    top: 46px;
  }
  .card--front .wordmark__name {
    font-size: 18px;
    width: 190px;
  }
  .holder {
    position: absolute;
    left: 50px;
    top: 148px;
    font-size: 21px;
    font-weight: 700;
    color: var(--ink);
  }
  .divider {
    position: absolute;
    left: 50px;
    right: 44px;
    top: 184px;
    height: 2px;
    background: var(--blue);
  }
  .contacts {
    position: absolute;
    right: 44px;
    top: 200px;
    list-style: none;
    text-align: right;
  }
  .contacts li {
    display: flex;
    justify-content: flex-end;
    align-items: center;
    gap: 8px;
    font-size: 14px;
    font-weight: 500;
    color: var(--ink-soft);
    line-height: 26px;
  }
  .contacts svg { width: 15px; height: 15px; flex: none; }

  /* back */
  .card--back .wordmark {
    position: absolute;
    left: 0; right: 0; top: 0; bottom: 0;
    justify-content: center;
  }
  .card--back .wordmark__dot { width: 22px; height: 22px; }
  .card--back .wordmark__name {
    font-size: 34px;
    text-align: left;
  }
</style>
</head>
<body>
<main class="stage">

  <section class="card card--front" aria-label="Business card front">
    <div class="wordmark">
      <span class="wordmark__dot"></span>
      <span class="wordmark__name">Brisk 'N' Bright Electrical</span>
    </div>

    <p class="holder">Darren Kolovos</p>
    <div class="divider"></div>

    <ul class="contacts">
      <li>0427 381 592
        <svg viewBox="0 0 16 16" aria-hidden="true">
          <circle cx="8" cy="8" r="7" fill="none" stroke="var(--blue)" stroke-width="1.6"/>
          <path d="M5.2 4.6c.4-.3.9-.2 1.1.2l.6 1.2c.2.3.1.7-.2.9l-.4.3c.4.9 1.1 1.6 2 2l.3-.4c.2-.3.6-.4.9-.2l1.2.6c.4.2.5.7.2 1.1-.6.8-1.5 1-2.4.6-1.6-.7-2.9-2-3.6-3.6-.4-.9-.2-1.8.3-2.7z" fill="var(--blue)"/>
        </svg>
      </li>
      <li>Brisknbrightelectrical@mailvane.com
        <svg viewBox="0 0 16 16" aria-hidden="true">
          <rect x="1" y="3" width="14" height="10" rx="1" fill="var(--blue)"/>
          <path d="M1.5 3.8 8 9l6.5-5.2" fill="none" stroke="var(--paper)" stroke-width="1.3"/>
        </svg>
      </li>
      <li>Brisknbrightelectrical.com.au
        <svg viewBox="0 0 16 16" aria-hidden="true">
          <circle cx="8" cy="8" r="7" fill="var(--blue)"/>
          <path d="M1.5 8h13M8 1.2c-2.2 2-2.2 11.6 0 13.6M8 1.2c2.2 2 2.2 11.6 0 13.6M2.6 4.6h10.8M2.6 11.4h10.8" fill="none" stroke="var(--paper)" stroke-width="0.9"/>
        </svg>
      </li>
    </ul>
  </section>

  <section class="card card--back" aria-label="Business card back">
    <div class="wordmark">
      <span class="wordmark__dot"></span>
      <span class="wordmark__name">Brisk 'N' Bright<br>Electrical</span>
    </div>
  </section>

</main>
</body>
</html>
```